Amber Ladle Whimsy Website Design; Cupcake Business with a unique and bespoke design element

We need a website design for a new bespoke and unique business making gourmet cupcakes - but MOST IMPORTANTLY we design and handmake cupcake wrappers and toppers specifically for each client's event. We are based in Sydney, Australia. The final resulting website should be elegant yet whimsical reflecting the notion of dreams and very elegant events eg weddings and very special parties.

We want to eventually have about 5 pages, HOWEVER, this project is specifically for the first page (ie Home page) and one other only. The final required pages are: a HOME page; ABOUT US page; PHOTO GALLERY page; FLAVOUR MENU & OTHER PRODUCTS page; CONTACT & INTERNET ENQUIRY page.

We expect the HOME page to be quite elaborate, perhaps including some animation. We will be providing the text content for all the other pages, and basically they will have the same background as the home page. We are looking for a clean design that runs across each page thus giving the website a continuity that pulls it all together. We would like our logo to be included on each page.

PLEASE NOTE: We will want multiple pages worked on in the handover phase but initially we want a very concise, consistent template to limit the amount of work to prospective designers.

While we are primarily looking for the design phase to be covered by this project, we would certainly appreciate coding to be included and will take that into consideration when choosing a winner.

Hi Designers

We have added some more information to our brief - please review it.

Thanks and happy designing

Hi Designers

Please note that we have increased our Prize money to $750.00.  We hope this encourages you to participate.

Thanks and regards
Amber Ladle Whimsy

Hi Designers

We've just posted some photos to help give you an idea of what we do.  Please note our attention to detail and precision in our work.

Thanks
Amber Ladle Whimsy

Hi Designers

Please Note:  What makes us different  to any other cupcake business is that we design cupcake wrappers and toppers, unique to our client's event whether it be a wedding, a birthday party or product launch.  We consult with our client to understand themes, colours, styles etc.  We then have our designs printed, next they are cut by a specialised computerised cutting machine,  We assemble everything by hand, and usually embellish the wrapper and topper with pearls, crystals, feathers, lace, ribbons or whatever else is appropriate for the event.  All work is totally bespoke, unique and individual.  No other cupcake supplier that we know of goes to these lengths to satisfy their client's dreams.

THE WRAPPER AND TOPPER IS OUR PRIMARY SELLING POINT. 

PLEASE NOTE:- We have uploaded a new photograph which we want to be used as the main photograph on the landing page.

We have removed all previous photographs of cupcakes (except for one that we can't get rid of).

We don't want a picture of a cupcake on the landing page we want the image _D7C3239.jpg to be used for that purpose.

We have also uploaded our logo in a number of file formats as we have had requests from you for these.

Hi designers

we have a crazy busy weekend on and won't be able to make any decisions re our competition until Monday  -  sorry to keep you in suspense, just a couple more days please!

regards
Meg

Target Market(s)

Primarily women - brides, new mothers (Christenings), Event Planners, who place an emphasis on the beauty of a product rather than the cost

Industry/Entity Type

Events

Requirements
Must have
• It must have our Logo (see attached upload) on each page (our logo is a butterfly atop a cupcake resting on a spoon and our motto is "Baking Charming Pieces of Craft". The colours used are pale pink, blue and chocolate brown and we'd expect these colours to be repeated in the final website.
The website must have a photo gallery which we can access and add to/change as our business grows.
We need a contact page which has an "internet enquiry form".
There should be a "Menu" page describing our cupcake flavours.
The Home page must have a party/event feel to it - definitely making an enquirer want to enter further into the site.
Nice to have
• Our logo is attached below in the "uploads". One idea that we have had is to use the butterfly in the logo but start it as a caterpillar crawling on the screen; as it spins it's cocoon the words "Gentle Slumber Tiny Grub" would appear on screen; this would incorporate the "Dreams" in our Business Name; then our logo butterfly would hatch. This encapsulates the idea of taking something plain (caterpillar/cupcake) and creating something beautiful (butterfly/OUR cupcake).
However, we are open to other design ideas.
The colours we would like to have are pale pink, blue and chocolate brown in the design.

Some websites we really admire are: www.dorawhitley.example www.glueribbontart.example.au and www.greetingsvera.example.au
These websites have a lightness and sense of fantasy to them. They do not convey a corporate image at all, rather they make you want to be at the party.
Should not have
• No "Corporate" style.

Most Important: We already have a website which we are not happy with - that is why we are going through this exercise to replace it. That means we DO NOT want anything along the lines of our current website. We are expecting some fresh ideas for our prize money.

```html
<!DOCTYPE html>
<html lang="en">
<head>
<meta charset="utf-8">
<title>Amber Ladle Whimsy — Home</title>
<link rel="stylesheet" href="https://fonts.googleapis.com/css2?family=Libre+Baskerville&family=Arimo:wght@400;700&display=swap">
<style>
  :root {
    --navy: #002b5c;
    --pink: #ee5fa7;
    --brown: #5a2a1a;
    --white: #ffffff;
    --paper: #f4f3f1;
    --tab-grey: #eeeeee;
    --icon-grey: #f2f2f2;
    --dot-white: #ffffff;
  }
  * { margin: 0; padding: 0; box-sizing: border-box; }
  html, body { width: 1200px; height: 896px; overflow: hidden; background: var(--white); }
  .page { position: relative; width: 1200px; height: 896px; overflow: hidden; font-family: "Arimo", Arial, sans-serif; }

  .top-band { position: absolute; left: 0; top: 0; width: 1200px; height: 14px; background: var(--navy); }
  .top-rule { position: absolute; left: 0; top: 14px; width: 1200px; height: 3px; background: var(--pink); }

  .backdrop {
    position: absolute; left: 0; top: 184px; width: 1200px; height: 632px;
    background:
      linear-gradient(180deg, rgba(255,255,255,1) 0%, rgba(255,255,255,0) 14%, rgba(255,255,255,0) 86%, rgba(255,255,255,1) 100%),
      linear-gradient(90deg, #8a7a66 0%, #cfc8bf 10%, #ebe8e4 30%, #e7e3de 70%, #bdb8b2 90%, #8d8b88 100%);
  }

  .brand {
    position: absolute; left: 460px; top: 30px; width: 280px; height: 162px;
    display: flex; flex-direction: column; align-items: center; justify-content: center; gap: 10px;
    background: var(--white);
  }
  .brand-dot { width: 54px; height: 54px; border-radius: 50%; background: var(--pink); opacity: .85; }
  .brand-name { font-family: "Libre Baskerville", Georgia, serif; font-size: 24px; color: var(--brown); white-space: nowrap; }
  .brand-motto { font-family: "Libre Baskerville", Georgia, serif; font-size: 11px; color: var(--brown); }

  .nav-bar {
    position: absolute; left: 106px; top: 201px; width: 989px; height: 56px;
    background: rgba(255,255,255,.82); border-radius: 6px 6px 0 0;
  }
  .nav-link {
    position: absolute; top: 195px; height: 59px; line-height: 64px;
    font-family: "Libre Baskerville", Georgia, serif; font-size: 20px; color: var(--navy); white-space: nowrap;
  }
  .nav-link.is-current { left: 188px; width: 111px; background: var(--navy); color: var(--white); text-align: center; border-radius: 2px 2px 0 0; }

  .social-button {
    position: absolute; top: 211px; width: 35px; height: 34px;
    background: var(--icon-grey); border-radius: 4px; box-shadow: 0 1px 2px rgba(0,0,0,.25);
  }

  .content-panel {
    position: absolute; left: 106px; top: 259px; width: 989px; height: 491px;
    background: var(--white); border-radius: 0 0 10px 10px; box-shadow: 0 2px 6px rgba(0,0,0,.15);
  }
  .intro-text {
    position: absolute; left: 145px; top: 289px; width: 285px;
    font-size: 15px; line-height: 22.2px; color: var(--navy);
  }
  .hero-photo {
    position: absolute; left: 441px; top: 280px; width: 634px; height: 444px;
    background: radial-gradient(ellipse at 50% 45%, #cdb89a 0%, #b9a68d 30%, #8f8478 60%, #d9d6d2 100%);
  }
  .slide-dot { position: absolute; top: 297px; width: 19px; height: 19px; border-radius: 50%; background: var(--dot-white); box-shadow: 0 1px 2px rgba(0,0,0,.3); }
  .slide-dot.is-active { background: var(--navy); }

  .footer-rule { position: absolute; left: 0; top: 816px; width: 1200px; height: 5px; background: var(--pink); }
  .footer { position: absolute; left: 0; top: 821px; width: 1200px; height: 75px; background: var(--navy); }
  .copyright { position: absolute; left: 0; top: 854px; width: 1202px; text-align: center; font-size: 11px; font-weight: 700; color: var(--white); }
  .sound-icon { position: absolute; left: 964px; top: 840px; }
  .sound-toggle { position: absolute; left: 1015px; top: 855px; font-size: 14px; font-weight: 700; color: var(--white); }
</style>
</head>
<body>
<div class="page">
  <div class="top-band"></div>
  <div class="top-rule"></div>

  <div class="backdrop" role="img" aria-label="Soft photograph of lace, ribbons, feathers and paper roses on a table"></div>

  <div class="brand">
    <div class="brand-dot"></div>
    <div class="brand-name">Amber Ladle Whimsy</div>
    <div class="brand-motto">Baking Charming Pieces of Craft</div>
  </div>

  <div class="nav-bar"></div>
  <nav>
    <span class="nav-link is-current">Home</span>
    <span class="nav-link" style="left:322px">About Us</span>
    <span class="nav-link" style="left:449px">Gallery</span>
    <span class="nav-link" style="left:569px">Flavour Menu</span>
    <span class="nav-link" style="left:744px">Contact Us</span>
  </nav>
  <span class="social-button" style="left:899px" aria-label="Social link"></span>
  <span class="social-button" style="left:950px" aria-label="Social link"></span>
  <span class="social-button" style="left:1003px" aria-label="Social link"></span>

  <div class="content-panel"></div>
  <p class="intro-text">What makes us different&nbsp; to any other cupcake business is that we design cupcake wrappers and toppers, unique to our client's event whether it be a wedding, a birthday party or product launch.&nbsp; We consult with our client to understand themes, colours, styles etc. We then have our designs printed, next they are cut by a specialised computerised cutting machine,&nbsp; We assemble everything by hand, and usually embellish the wrapper and topper with pearls, crystals, feathers, lace, ribbons or whatever else is appropriate for the event.&nbsp; All work is totally bespoke, unique and individual.&nbsp; No other cupcake supplier that we know of goes to these lengths to satisfy their client's dreams.</p>

  <div class="hero-photo" role="img" aria-label="Workbench with paper roses, pearls, crystals, feathers, ribbons and scissors for cupcake toppers"></div>
  <span class="slide-dot is-active" style="left:941px"></span>
  <span class="slide-dot" style="left:972px"></span>
  <span class="slide-dot" style="left:1004px"></span>
  <span class="slide-dot" style="left:1033px"></span>

  <div class="footer-rule"></div>
  <footer class="footer"></footer>
  <p class="copyright">© Copyright 2012&nbsp; |&nbsp; Amber Ladle Whimsy&nbsp; |&nbsp; All Rights Reserved</p>
  <svg class="sound-icon" width="38" height="32" viewBox="0 0 38 32" aria-label="Sound">
    <rect x="0" y="18" width="5" height="14" fill="#fff"/>
    <rect x="8" y="12" width="5" height="20" fill="#fff"/>
    <rect x="16" y="6" width="5" height="26" fill="#fff"/>
    <rect x="24" y="0" width="5" height="32" fill="#fff"/>
    <rect x="32" y="9" width="5" height="23" fill="#fff"/>
  </svg>
  <span class="sound-toggle">OFF&nbsp; |&nbsp; ON</span>
</div>
</body>
</html>
```